Brenlo Auction Flyer

August 24th thru 27th Online only farm and construction equipment auction Held at brenlo auction service Now accepting consignments
Contact Marcus at 810-627-3148 Or Email Marcus@brenloauction-example.com
Accepting consignment now thru August 20th

Auction Business

```html
<!DOCTYPE html>
<html lang="en">
<head>
<meta charset="utf-8">
<title>Brenlo Auction – Farm and Construction Equipment Auction</title>
<link rel="stylesheet" href="https://fonts.googleapis.com/css2?family=Anton&family=Oswald:wght@500;700&display=swap">
<style>
  :root {
    --orange: #f4921f;
    --orange-dark: #e37f12;
    --grey: #8c8c8c;
    --grey-dark: #6f7071;
    --ink: #1e1e1e;
    --white: #ffffff;
    --slate: #5b6572;
    --page: #b9babc;
  }
  * { margin: 0; padding: 0; box-sizing: border-box; }
  html, body { width: 1200px; height: 2640px; overflow: hidden; background: var(--page); }
  .flyer {
    position: absolute; left: 40px; top: 597px;
    width: 1120px; height: 1445px;
    background: var(--grey);
    overflow: hidden;
    box-shadow: 8px 10px 18px rgba(0,0,0,.35);
    font-family: "Anton", "Oswald", sans-serif;
  }
  .hero-photo {
    position: absolute; left: 0; top: 0; width: 1120px; height: 601px;
    background: linear-gradient(180deg, #ffffff 0%, #f4f7fb 22%, #a8c4e4 44%, #c9d1da 58%, #8b8e90 72%, #5c5d5c 100%);
  }
  .brand {
    position: absolute; left: 0; right: 0; top: 150px;
    display: flex; align-items: center; justify-content: center; gap: 16px;
  }
  .brand-dot { width: 40px; height: 40px; border-radius: 50%; background: var(--orange); }
  .brand-name { font-size: 52px; color: var(--orange); letter-spacing: .5px; }

  .title-band {
    position: absolute; left: 0; top: 601px; width: 1120px; height: 289px;
    background: var(--orange);
  }
  .title-line {
    position: absolute; left: 0; right: 0; text-align: center;
    color: var(--white); text-shadow: 4px 4px 0 var(--ink);
    letter-spacing: -1px; line-height: 1;
  }
  .title-line.one { top: 32px; font-size: 92px; }
  .title-line.two { top: 125px; font-size: 114px; }

  .divider { position: absolute; left: 0; top: 890px; width: 1120px; height: 8px; background: var(--white); }
  .pill {
    position: absolute; left: 375px; top: 857px; width: 370px; height: 78px;
    border-radius: 39px; background: var(--white); border: 4px solid var(--orange);
    display: flex; align-items: center; justify-content: center; gap: 10px;
    font-size: 50px; line-height: 1;
  }
  .pill .hi { color: var(--orange); }
  .pill .lo { color: var(--grey-dark); }

  .ground {
    position: absolute; left: 0; top: 898px; width: 1120px; height: 440px;
    background: linear-gradient(180deg, #7d7e7f 0%, #939495 55%, #838485 100%);
  }
  .cart-photo {
    position: absolute; left: 320px; top: 960px; width: 460px; height: 378px;
    background: radial-gradient(ellipse at 50% 55%, #3a3d40 0%, #55585b 50%, rgba(140,140,140,0) 75%);
  }

  .dates { position: absolute; left: 53px; top: 990px; width: 240px; text-align: center; }
  .dates svg { display: block; margin: 0 auto 10px; }
  .days { font-size: 62px; color: var(--white); line-height: 1; }
  .days sup { font-size: 30px; vertical-align: top; position: relative; top: 4px; }
  .days .dash { color: var(--orange); }
  .month { font-size: 80px; color: var(--orange); line-height: 1.05; }
  .year { font-family: "Oswald", sans-serif; font-weight: 700; font-size: 44px; color: var(--white); letter-spacing: 12px; line-height: 1.2; }

  .badge {
    position: absolute; left: 779px; top: 994px; width: 282px; height: 282px;
    border-radius: 50%; background: var(--white);
    display: flex; align-items: center; justify-content: center;
  }
  .badge-inner {
    width: 248px; height: 248px; border-radius: 50%; background: var(--orange);
    display: flex; flex-direction: column; align-items: center; justify-content: center;
    color: var(--white); text-align: center; line-height: 1.05;
  }
  .badge-inner .big { font-size: 42px; }
  .badge-inner .mid { font-size: 30px; }
  .deadline { margin-top: 10px; background: var(--white); padding: 6px 20px 4px; }
  .deadline .thru { font-family: "Oswald", sans-serif; font-weight: 500; font-size: 22px; color: var(--grey-dark); }
  .deadline .day { font-size: 46px; color: var(--orange); }

  .contact-bar {
    position: absolute; left: 0; top: 1338px; width: 1120px; height: 84px;
    background: var(--white); display: flex; align-items: center;
  }
  .contact-tag {
    width: 370px; height: 84px; background: var(--orange);
    border-radius: 0 42px 42px 0;
    display: flex; align-items: center; padding-left: 56px;
    font-size: 40px; color: var(--white);
  }
  .contact-tag .name { color: var(--ink); margin-left: 10px; }
  .contact-item {
    display: flex; align-items: center; gap: 8px;
    font-family: "Oswald", sans-serif; font-weight: 700; font-size: 29px; color: var(--slate);
  }
  .contact-item.phone { margin-left: 30px; }
  .contact-item.email { margin-left: 40px; }
</style>
</head>
<body>
<main class="flyer">
  <div class="hero-photo" role="img" aria-label="Photo of compact excavators, golf carts and a tracked dumper lined up on gravel in front of storage containers under a blue sky"></div>

  <div class="brand">
    <span class="brand-dot"></span>
    <span class="brand-name">BRENLO AUCTION SERVICE</span>
  </div>

  <section class="title-band">
    <h1>
      <span class="title-line one">FARM AND CONSTRUCTION</span>
      <span class="title-line two">EQUIPMENT AUCTION</span>
    </h1>
  </section>

  <div class="ground"></div>
  <div class="divider"></div>
  <div class="pill"><span class="hi">ONLINE</span><span class="lo">ONLY</span></div>

  <div class="cart-photo" role="img" aria-label="Photo of a dark grey four-seat golf cart with a windshield and roof"></div>

  <div class="dates">
    <svg width="86" height="86" viewBox="0 0 86 86" aria-hidden="true">
      <circle cx="43" cy="43" r="40" fill="none" stroke="#f4921f" stroke-width="3"/>
      <rect x="24" y="27" width="38" height="34" rx="4" fill="none" stroke="#f4921f" stroke-width="3"/>
      <line x1="24" y1="36" x2="62" y2="36" stroke="#f4921f" stroke-width="3"/>
      <line x1="32" y1="22" x2="32" y2="31" stroke="#f4921f" stroke-width="3"/>
      <line x1="54" y1="22" x2="54" y2="31" stroke="#f4921f" stroke-width="3"/>
      <g fill="#f4921f">
        <rect x="30" y="42" width="5" height="5"/><rect x="40" y="42" width="5" height="5"/><rect x="50" y="42" width="5" height="5"/>
        <rect x="30" y="51" width="5" height="5"/><rect x="40" y="51" width="5" height="5"/>
      </g>
    </svg>
    <div class="days">24<sup>th</sup> <span class="dash">-</span> 27<sup>th</sup></div>
    <div class="month">AUGUST</div>
    <div class="year">2026</div>
  </div>

  <div class="badge">
    <div class="badge-inner">
      <span class="big">ACCEPTING</span>
      <span class="mid">CONSIGNMENT</span>
      <div class="deadline">
        <div class="thru">Thru August</div>
        <div class="day">20th</div>
      </div>
    </div>
  </div>

  <footer class="contact-bar">
    <div class="contact-tag">Contact <span class="name">Marcus</span></div>
    <div class="contact-item phone">
      <svg width="26" height="26" viewBox="0 0 24 24" aria-hidden="true"><path fill="#f4921f" d="M6.6 10.8a15.1 15.1 0 0 0 6.6 6.6l2.2-2.2c.3-.3.7-.4 1-.2 1.1.4 2.3.6 3.6.6.6 0 1 .4 1 1V20c0 .6-.4 1-1 1A17 17 0 0 1 3 4c0-.6.4-1 1-1h3.5c.6 0 1 .4 1 1 0 1.3.2 2.5.6 3.6.1.3 0 .7-.2 1z"/></svg>
      810-627-3148
    </div>
    <div class="contact-item email">
      <svg width="30" height="22" viewBox="0 0 30 22" aria-hidden="true"><rect width="30" height="22" rx="2" fill="#f4921f"/><path d="M2 3l13 10L28 3" fill="none" stroke="#fff" stroke-width="2.5"/></svg>
      Marcus@brenloauction-example.com
    </div>
  </footer>
</main>
</body>
</html>
```